5 post cards for B2B Advertising

We are an electrical lighting contractor advertising our Lighting and Electrical services to property management companies, car dealer ships, hotels, schools, malls, and shopping centers.

RED / White / Blue themed American flag.

Post Cards

1. Electrical Services
2. Lighting Services and conversions to LED
3. Sign Repairs and conversions to LED
4. Nighttime Lighting Inspections (report lights and signs out)
5. Lighting is Safety

```html
<!DOCTYPE html>
<html lang="en">
<head>
<meta charset="utf-8">
<title>Brightline Electric – Electrical Services Postcard</title>
<link rel="stylesheet" href="https://fonts.googleapis.com/css2?family=Oswald:wght@500;700&family=Roboto:wght@400;500;700&display=swap">
<style>
  :root{
    --backdrop:#3b3b3d;
    --navy:#1b2f6b;
    --blue:#1f4aa0;
    --red:#d7262e;
    --white:#ffffff;
    --ink:#27324a;
    --gold:#e2a72a;
    --paper:#f4f5f7;
  }
  *{box-sizing:border-box;margin:0;padding:0}
  html,body{width:719px;height:1200px;overflow:hidden;background:var(--backdrop)}
  body{position:relative;font-family:"Roboto",Arial,sans-serif}
  .postcard{position:absolute;left:80px;width:560px;height:360px;background:var(--white);overflow:hidden;box-shadow:0 10px 24px rgba(0,0,0,.45)}
  .postcard--front{top:200px}
  .postcard--back{top:600px}
  .layer{position:absolute;left:0;top:0}
  .brand{position:absolute;font-family:"Oswald",Arial,sans-serif;font-weight:700;color:var(--red);letter-spacing:.5px;line-height:1}
  .front__brand{left:18px;top:16px;font-size:19px}
  .front__values{position:absolute;left:18px;top:44px;width:240px;font-size:6.5px;line-height:1.35;color:var(--ink)}
  .front__headline{position:absolute;left:18px;top:72px;width:245px;font-family:"Oswald",Arial,sans-serif;font-weight:700;font-size:26px;line-height:1.1;color:var(--blue);text-transform:uppercase}
  .front__location{position:absolute;left:0;top:222px;width:268px;height:30px;background:var(--red);color:var(--white);font-family:"Oswald",Arial,sans-serif;font-weight:700;font-size:18px;line-height:30px;padding-left:18px;white-space:nowrap}
  .front__quote{position:absolute;right:0;top:244px;width:220px;height:42px;background:var(--red);color:var(--white);font-family:"Oswald",Arial,sans-serif;font-weight:700;font-size:22px;line-height:42px;text-align:center}
  .contact{position:absolute;display:flex;align-items:center;gap:8px;color:var(--white)}
  .contact__phone{font-family:"Oswald",Arial,sans-serif;font-weight:700;font-size:21px;line-height:1}
  .contact__small{font-size:9px;line-height:1.35}
  .front__contact{left:18px;top:302px}
  .front__address{left:300px;top:300px}
  .back__tab{position:absolute;left:0;top:16px;width:220px;height:30px;background:var(--navy);color:var(--white);font-family:"Oswald",Arial,sans-serif;font-weight:700;font-size:17px;line-height:30px;padding-left:18px}
  .back__tab::after{content:"";position:absolute;right:-10px;top:0;width:10px;height:30px;background:var(--red)}
  .services{position:absolute;left:18px;top:58px;list-style:none}
  .services li{display:flex;align-items:center;gap:6px;font-size:10px;line-height:17px;color:var(--ink)}
  .back__quote{position:absolute;left:0;top:248px;width:240px;height:30px;background:var(--red);color:var(--white);font-family:"Oswald",Arial,sans-serif;font-weight:700;font-size:17px;line-height:30px;padding-left:18px}
  .back__contactbar{position:absolute;left:0;top:288px;width:260px;height:52px;background:var(--navy)}
  .back__contact{left:18px;top:296px}
  .back__brand{right:30px;top:298px;font-size:20px}
  .stamp{position:absolute;right:24px;top:18px;width:58px;height:66px;border:1.5px solid #9aa3b5}
</style>
</head>
<body>

<section class="postcard postcard--front">
  <svg class="layer" width="560" height="360" viewBox="0 0 560 360" role="img" aria-label="Photo of an electrician in a high-visibility vest working on conduit">
    <defs>
      <linearGradient id="photoTone" x1="0" y1="0" x2="1" y2="1">
        <stop offset="0" stop-color="#c9cfd6"/>
        <stop offset=".5" stop-color="#b6c34a"/>
        <stop offset="1" stop-color="#6f7780"/>
      </linearGradient>
    </defs>
    <path d="M330 0 H560 V280 H296 Q282 130 330 0 Z" fill="url(#photoTone)"/>
  </svg>
  <svg class="layer" width="560" height="360" viewBox="0 0 560 360" aria-hidden="true">
    <path d="M322 0 Q274 130 288 280" fill="none" stroke="var(--red)" stroke-width="8"/>
    <path d="M310 0 Q262 130 276 280" fill="none" stroke="var(--navy)" stroke-width="6"/>
    <rect x="0" y="280" width="560" height="80" fill="var(--navy)"/>
    <rect x="0" y="280" width="560" height="3" fill="var(--red)"/>
  </svg>

  <div class="brand front__brand">BRIGHTLINE ELECTRIC INC.</div>
  <p class="front__values">Since 1961, everything we do is guided by our core values: HONESTY | QUALITY | RESPECT | SAFETY | SERVICE | CARE</p>
  <h1 class="front__headline">Professional<br>Residential and<br>Commercial<br>Electrical Services</h1>
  <div class="front__location">BASED IN ALEXANDRIA, VA</div>
  <div class="front__quote">GET A FREE QUOTE</div>

  <div class="contact front__contact">
    <svg width="26" height="26" viewBox="0 0 24 24" aria-hidden="true"><path fill="#fff" d="M6.6 10.8a15 15 0 0 0 6.6 6.6l2.2-2.2c.3-.3.7-.4 1-.2 1.1.4 2.3.6 3.6.6.6 0 1 .4 1 1V20c0 .6-.4 1-1 1A17 17 0 0 1 3 4c0-.6.4-1 1-1h3.5c.6 0 1 .4 1 1 0 1.3.2 2.5.6 3.6.1.3 0 .7-.2 1z"/></svg>
    <div>
      <div class="contact__phone">+1 (800) 555-0147</div>
      <div class="contact__small">info@brightlineelectric.com</div>
    </div>
  </div>
  <div class="contact front__address">
    <svg width="14" height="20" viewBox="0 0 14 20" aria-hidden="true"><path fill="#fff" d="M7 0a7 7 0 0 0-7 7c0 5 7 13 7 13s7-8 7-13a7 7 0 0 0-7-7zm0 9.5A2.5 2.5 0 1 1 7 4.5a2.5 2.5 0 0 1 0 5z"/></svg>
    <div class="contact__small">4820 Harbor Ln<br>Alexandria, VA 22310<br>www.brightlineelectric.com</div>
  </div>
</section>

<section class="postcard postcard--back">
  <svg class="layer" width="560" height="360" viewBox="0 0 560 360" aria-hidden="true">
    <path d="M250 0 Q300 180 262 360 H250 Q288 180 238 0 Z" fill="var(--red)"/>
    <path d="M262 0 Q312 180 274 360 H266 Q304 180 254 0 Z" fill="var(--navy)"/>
    <path d="M274 0 Q324 180 286 360 H278 Q316 180 266 0 Z" fill="#dfe3ea"/>
  </svg>
  <svg class="layer" style="left:0;top:138px" width="250" height="100" viewBox="0 0 250 100" role="img" aria-label="Photos of commercial lighting installation and service trucks">
    <defs>
      <linearGradient id="stripTone" x1="0" y1="0" x2="1" y2="0">
        <stop offset="0" stop-color="#b78a5a"/>
        <stop offset=".5" stop-color="#e6dccd"/>
        <stop offset="1" stop-color="#8d98a6"/>
      </linearGradient>
    </defs>
    <rect width="250" height="100" fill="url(#stripTone)"/>
    <rect x="98" y="0" width="3" height="100" fill="#fff"/>
  </svg>

  <div class="back__tab">ELECTRICAL SERVICES</div>
  <ul class="services">
    <li><svg width="10" height="10" viewBox="0 0 10 10" aria-hidden="true"><path d="M1 5l3 3 5-6" fill="none" stroke="var(--red)" stroke-width="2"/></svg>Commercial installations &amp; upgrades</li>
    <li><svg width="10" height="10" viewBox="0 0 10 10" aria-hidden="true"><path d="M1 5l3 3 5-6" fill="none" stroke="var(--red)" stroke-width="2"/></svg>Preventive maintenance</li>
    <li><svg width="10" height="10" viewBox="0 0 10 10" aria-hidden="true"><path d="M1 5l3 3 5-6" fill="none" stroke="var(--red)" stroke-width="2"/></svg>Emergency repairs 24/7</li>
    <li><svg width="10" height="10" viewBox="0 0 10 10" aria-hidden="true"><path d="M1 5l3 3 5-6" fill="none" stroke="var(--red)" stroke-width="2"/></svg>Code compliance &amp; safety inspections</li>
  </ul>
  <div class="back__quote">REQUEST A FREE QUOTE</div>
  <div class="back__contactbar"></div>
  <div class="contact back__contact">
    <svg width="24" height="24" viewBox="0 0 24 24" aria-hidden="true"><path fill="#fff" d="M6.6 10.8a15 15 0 0 0 6.6 6.6l2.2-2.2c.3-.3.7-.4 1-.2 1.1.4 2.3.6 3.6.6.6 0 1 .4 1 1V20c0 .6-.4 1-1 1A17 17 0 0 1 3 4c0-.6.4-1 1-1h3.5c.6 0 1 .4 1 1 0 1.3.2 2.5.6 3.6.1.3 0 .7-.2 1z"/></svg>
    <div>
      <div class="contact__phone">+1 (800) 555-0147</div>
      <div class="contact__small">info@brightlineelectric.com</div>
    </div>
  </div>

  <svg class="layer" style="left:272px;top:232px" width="64" height="64" viewBox="0 0 64 64" aria-hidden="true">
    <circle cx="32" cy="32" r="30" fill="var(--gold)"/>
  </svg>
  <div class="stamp"></div>
  <div class="brand back__brand">BRIGHTLINE ELECTRIC INC.</div>
</section>

</body>
</html>
```